Ferncrest Dental, LLC business card project

Business card to be designed with current logo.
Dental office- please keep design of card that looks clean and professional.
Please include the following info:
Ferncrest Dental, LLC
Dr. Lorna Pettigrew
2871 Marlowe Street
Bethlehem, PA 18093
610-555-0193
ferncrestdental.office@examplemail.test
Hello everyone-
Reason: Just got back from overseas- will look at all designs and provide feedback. Thank you!
Reason: Polling my friends for the final selection-
thank you to all those that participated- so many talented designers!

```html
<!DOCTYPE html>
<html lang="en">
<head>
<meta charset="utf-8">
<title>Ferncrest Dental, LLC — Business Card</title>
<link rel="stylesheet" href="https://fonts.googleapis.com/css2?family=Questrial&family=Arimo:wght@700&display=swap">
<style>
  :root {
    --lime: #b5d334;
    --lime-deep: #a9c92e;
    --band: #000000;
    --white: #ffffff;
  }
  html, body {
    margin: 0;
    padding: 0;
    width: 1200px;
    height: 686px;
    overflow: hidden;
    background: var(--lime);
  }
  .card {
    position: relative;
    width: 1200px;
    height: 686px;
    background: var(--lime);
    overflow: hidden;
  }
  .card__band {
    position: absolute;
    inset: 0;
    width: 1200px;
    height: 686px;
  }
  .brand {
    position: absolute;
    left: 40px;
    top: 232px;
    display: flex;
    align-items: center;
    gap: 28px;
  }
  .brand__dot {
    width: 64px;
    height: 64px;
    border-radius: 50%;
    background: var(--lime);
    flex: none;
  }
  .brand__name {
    font-family: "Questrial", sans-serif;
    font-size: 84px;
    line-height: 1;
    color: var(--lime);
    white-space: nowrap;
    letter-spacing: -0.5px;
  }
  .contact {
    position: absolute;
    left: 0;
    right: 0;
    top: 424px;
    text-align: center;
    color: var(--white);
  }
  .contact__name {
    font-family: "Arimo", sans-serif;
    font-weight: 700;
    font-size: 36px;
    line-height: 1;
    margin: 0 0 24px;
    padding-left: 10px;
  }
  .contact__line {
    font-family: "Questrial", sans-serif;
    font-size: 31px;
    line-height: 1.4;
    margin: 0;
    white-space: nowrap;
  }
</style>
</head>
<body>
  <main class="card">
    <svg class="card__band" viewBox="0 0 1200 686" aria-hidden="true">
      <path d="M0,212 Q520,20 1200,34 L1200,382 Q640,362 0,396 Z" fill="var(--band)"/>
    </svg>

    <div class="brand">
      <span class="brand__dot"></span>
      <span class="brand__name">Ferncrest Dental, LLC</span>
    </div>

    <section class="contact">
      <p class="contact__name">Dr. Lorna Pettigrew</p>
      <p class="contact__line">2871 Marlowe Street, Bethlehem, PA 18093</p>
      <p class="contact__line">ph: 610-555-0193 &nbsp;|&nbsp; e-mail: ferncrestdental.office@examplemail.test</p>
    </section>
  </main>
</body>
</html>
```